Food Festival "Signature Cocktail" Booth Banner

Need a 3'x9'6" (36" tall x 114" wide) Outdoor Banner for a new "Signature Cocktail" booth at an outdoor food festival. Marlowe Onion Jubilee is a non profit festival and the World Record largest Garlic Festival with average of 100K attendees over 3 days. Actual drink served will vary from year to year, but banner for the booth with be reused each year so it will be non drink specific. Banner needs to catch attendee's attention both at a quick glance and from a distance outdoors to drive traffic and sales to the booth. It will be mounted above the sales window of a 10x10 Festival Booth on PVC frame (see attached pic for reference). "Signature Cocktail" is required text along with it being identified as a Marlowe Onion Jubilee booth either through use of attached logo (color can be modified) or "Marlowe Onion Jubilee" text since we also have for profit competing vendors. Banner will be full color print. Idea concepts: Neon Sign, Art Deco elegant, reclaimed wood...but open to any concepts. Festival website: https://marloweonionjubilee.example

Target Market(s)

Food Festival Attendees

Font styles to use
Decorative
Script
Other font styles liked:
• Neon, heavy weight fonts, open.

Colors

Designer to choose colors to be used in the design.

Requirements
Must have
• "Signature Cocktail" and "Marlowe Onion Jubilee" text or MOJ Logo provided, colors and layout that stands out and easily identifiable and readable from a long distance with strong text
Nice to have
• Vibrant engaging background,, ties to Garlic
Should not have
• Clip art, generic text

```html
<!DOCTYPE html>
<html lang="en">
<head>
<meta charset="UTF-8">
<title>Signature Cocktail – Marlowe Onion Jubilee Booth Banner</title>
<link rel="stylesheet" href="https://fonts.googleapis.com/css2?family=Josefin+Sans:wght@600&family=Playball&display=swap">
<style>
  :root {
    --page: #ececec;
    --wall-dark: #141212;
    --wall-mid: #221e1d;
    --neon-core: #ffd9b0;
    --neon-glow: #ff7a1a;
    --neon-edge: #ff9a3c;
    --copper: #9a5a32;
    --drink-deep: #a82a0c;
    --drink-bright: #e5541c;
  }
  * { margin: 0; padding: 0; box-sizing: border-box; }
  html, body {
    width: 1200px;
    height: 423px;
    overflow: hidden;
    background: var(--page);
  }
  .canvas {
    position: relative;
    width: 1200px;
    height: 423px;
    background: var(--page);
  }
  .banner {
    position: absolute;
    left: 20px;
    top: 28px;
    width: 1158px;
    height: 364px;
    overflow: hidden;
    background:
      radial-gradient(ellipse at 50% 40%, var(--wall-mid) 0%, var(--wall-dark) 70%);
    box-shadow: 0 1px 4px rgba(0, 0, 0, 0.35);
  }
  .wall-texture {
    position: absolute;
    inset: 0;
    background: linear-gradient(180deg, rgba(255,255,255,0.03), rgba(0,0,0,0.15));
  }
  .headline {
    position: absolute;
    left: 0;
    right: 0;
    top: 50px;
    text-align: center;
    font-family: "Josefin Sans", sans-serif;
    font-weight: 600;
    font-size: 112px;
    line-height: 1;
    letter-spacing: 0.14em;
    padding-left: 0.14em;
    color: var(--neon-core);
    text-shadow:
      0 0 2px var(--neon-edge),
      0 0 8px var(--neon-glow),
      0 0 18px var(--neon-glow),
      0 0 36px rgba(255, 122, 26, 0.6);
  }
  .subline {
    position: absolute;
    left: 0;
    right: 0;
    top: 168px;
    text-align: center;
    font-family: "Playball", cursive;
    font-size: 88px;
    line-height: 1;
    letter-spacing: 0.06em;
    color: var(--neon-core);
    text-shadow:
      0 0 2px var(--neon-edge),
      0 0 8px var(--neon-glow),
      0 0 18px var(--neon-glow),
      0 0 34px rgba(255, 122, 26, 0.55);
  }
  .festival-name {
    position: absolute;
    left: 26px;
    top: 188px;
    width: 150px;
    display: flex;
    flex-direction: column;
    align-items: center;
    gap: 10px;
    font-family: "Josefin Sans", sans-serif;
    font-weight: 600;
    font-size: 22px;
    line-height: 1.15;
    text-align: center;
    color: var(--copper);
  }
  .festival-name .mark {
    width: 40px;
    height: 40px;
    border-radius: 50%;
    background: var(--copper);
  }
  .drink-photo {
    position: absolute;
    left: 908px;
    top: 124px;
    width: 236px;
    height: 240px;
    background:
      radial-gradient(ellipse at 55% 55%, var(--drink-bright) 0%, var(--drink-deep) 45%, rgba(20,18,18,0) 72%);
  }
</style>
</head>
<body>
  <div class="canvas">
    <section class="banner">
      <div class="wall-texture"></div>
      <h1 class="headline">SIGNATURE</h1>
      <p class="subline">Cocktail</p>
      <div class="festival-name">
        <span class="mark"></span>
        <span>Marlowe Onion Jubilee</span>
      </div>
      <div class="drink-photo" role="img" aria-label="Photo of a red tomato cocktail splashing from a stemmed glass with cherry tomatoes"></div>
    </section>
  </div>
</body>
</html>
```